BrisaLink Systems Banner Stand Design

Looking for a banner stand design that is ready to print for an upcoming trade show. 33"x82" are the dimensions. It will need to catch the eye of those walking by our booth with a very generic description/bullet points of what/who we are. As a technology firm we like our printed material to be very crisp and new age as to say, we are are the forefront of our business.

Please refer to the attachments for more info.

Target Market(s)

Technical trade show attendees

Industry/Entity Type

Trade

Font styles to use
Sans Serif

Requirements
Must have
• Must have our logo, the majority of the design should be graphics, with 1/3 content that we will include, but it should consist of a sentence or two with about 8 bullet points. I have included our logo and our one-pager which will be printed and used in conjunction with the banner stand.
Nice to have
• As a tech firm that provides cloud and managed services we would like the graphics to be advanced so show that we are always keeping up with the ever growing tech field but that we also keep our customer as our main priority.
Should not have
• Should not have much room for content, we want to be able to use this at any event

```html
<!DOCTYPE html>
<html lang="en">
<head>
<meta charset="utf-8">
<title>BrisaLink Systems – Banner Stand</title>
<link href="https://fonts.googleapis.com/css2?family=Roboto+Condensed:wght@300;400;700&family=Roboto:wght@300;400&display=swap" rel="stylesheet">
<style>
  :root {
    --white: #ffffff;
    --ink: #1f2326;
    --brand-orange: #f26b1d;
    --panel-orange: #f58220;
    --panel-orange-light: #f9a03f;
    --footer-orange: #d8561a;
    --brand-blue: #1f9ad6;
    --band-blue: #2aa3db;
    --green: #8cc63f;
    --suit-dark: #14181d;
    --sky-light: #dfe8ef;
  }
  * { margin: 0; padding: 0; box-sizing: border-box; }
  html, body { width: 1200px; height: 2980px; overflow: hidden; background: var(--white); }
  .banner {
    position: relative; width: 1200px; height: 2980px; overflow: hidden;
    font-family: "Roboto Condensed", "Arial Narrow", sans-serif; color: var(--ink);
  }

  /* Brand */
  .brand { position: absolute; left: 140px; top: 84px; display: flex; align-items: center; gap: 44px; }
  .brand-mark { width: 256px; height: 256px; background: var(--brand-orange); border-radius: 36px; }
  .brand-name {
    font-family: "Roboto", sans-serif; font-weight: 300; color: var(--brand-orange);
    line-height: 1; display: flex; flex-direction: column; align-items: flex-end;
  }
  .brand-name-main { font-size: 148px; letter-spacing: -3px; }
  .brand-name-sub { font-size: 44px; margin-top: 6px; }

  /* Headline */
  .headline { position: absolute; left: 0; right: 0; top: 452px; text-align: center; text-transform: uppercase; }
  .headline-line { display: block; font-size: 92px; line-height: 1.12; font-weight: 300; color: var(--ink); }
  .headline-line.strong { font-weight: 700; }

  /* Image area */
  .scene {
    position: absolute; left: 0; top: 720px; width: 1200px; height: 1128px; overflow: hidden;
    background:
      linear-gradient(100deg, rgba(0,0,0,0) 55%, rgba(20,24,29,.85) 75%, var(--suit-dark) 100%),
      linear-gradient(170deg, var(--sky-light) 0%, #8fa6b8 30%, #3e5568 65%, #1d2a36 100%);
  }
  .tile { position: absolute; border-radius: 48px; border: 6px solid rgba(255,255,255,.9); box-shadow: 0 8px 24px rgba(0,0,0,.35); }
  .tile-office {
    left: 88px; top: 152px; width: 424px; height: 416px;
    background: linear-gradient(180deg, #f3f6f8 0%, #d7dee4 40%, #2a2d33 70%, #c9ced3 100%);
  }
  .tile-green {
    left: 552px; top: 152px; width: 420px; height: 416px;
    background: linear-gradient(150deg, rgba(140,198,63,.75), rgba(60,110,50,.8) 60%, rgba(20,30,20,.9));
  }
  .tile-airport {
    left: 88px; top: 612px; width: 424px; height: 420px;
    background: linear-gradient(180deg, #fbe2b0 0%, #f4b969 30%, #8c8f92 62%, #3a4048 82%, #1e232a 100%);
  }
  .tile-cloud {
    left: 540px; top: 600px; width: 600px; height: 500px;
    background: radial-gradient(circle at 45% 50%, #e6f7ff 0%, #7ccaf3 35%, #2c97dd 70%, #17609f 100%);
  }

  /* Services panel */
  .services {
    position: absolute; left: 0; top: 1848px; width: 1200px; height: 892px;
    background: var(--panel-orange); overflow: hidden;
  }
  .services-stripes { position: absolute; inset: 0; width: 1200px; height: 892px; }
  .services-title {
    position: absolute; left: 80px; top: 24px; width: 268px; height: 88px;
    background: var(--brand-blue); color: var(--white);
    font-size: 64px; font-weight: 400; line-height: 88px; padding-left: 20px;
  }
  .service-list { position: absolute; left: 80px; top: 120px; list-style: none; }
  .service-list li {
    display: flex; align-items: center; gap: 22px;
    height: 66px; font-size: 36px; color: var(--white);
  }
  .service-list svg { width: 30px; height: 30px; flex: none; }
  .feature-icons { position: absolute; left: 912px; top: 180px; display: flex; flex-direction: column; gap: 44px; }
  .feature-icon {
    width: 200px; height: 160px; background: var(--brand-blue);
    display: flex; align-items: center; justify-content: center;
  }
  .feature-icon svg { width: 110px; height: 110px; }

  /* Phone band & footer */
  .phone-band {
    position: absolute; left: 0; top: 2740px; width: 1200px; height: 100px;
    background: var(--band-blue); color: var(--white);
    text-align: center; font-size: 62px; font-weight: 300; line-height: 100px; letter-spacing: 2px;
  }
  .footer {
    position: absolute; left: 0; top: 2840px; width: 1200px; height: 140px;
    background: var(--footer-orange); color: var(--white);
    display: flex; justify-content: space-between; align-items: center;
    padding: 0 48px; font-size: 44px; font-weight: 400;
  }
</style>
</head>
<body>
<main class="banner">
  <header class="brand">
    <div class="brand-mark"></div>
    <div class="brand-name">
      <span class="brand-name-main">Brisa</span>
      <span class="brand-name-sub">Link Systems Corp.</span>
    </div>
  </header>

  <h1 class="headline">
    <span class="headline-line">Enterprise IT Services &amp;</span>
    <span class="headline-line strong">Cloud, Your Way...</span>
  </h1>

  <section class="scene" role="img" aria-label="Photo of a businessman in a dark suit with folded arms behind image tiles">
    <div class="tile tile-office" role="img" aria-label="Photo of a smiling businesswoman at a desk with a laptop"></div>
    <div class="tile tile-green" role="img" aria-label="Translucent green tile over the businessman's folded arms"></div>
    <div class="tile tile-airport" role="img" aria-label="Photo of an airport window at sunset with a plane taking off"></div>
    <div class="tile tile-cloud" role="img" aria-label="Illustration of a hand holding a cloud computing symbol with floating device icons"></div>
  </section>

  <section class="services">
    <svg class="services-stripes" viewBox="0 0 1200 892" preserveAspectRatio="none" aria-hidden="true">
      <polygon points="720,0 1200,0 1200,892 640,892" fill="#f9a03f"/>
      <polygon points="1010,0 1200,0 1200,892 930,892" fill="#8cc63f"/>
    </svg>
    <h2 class="services-title">SERVICES</h2>
    <ul class="service-list">
      <li><svg viewBox="0 0 30 30"><rect x="3" y="3" width="18" height="18" fill="none" stroke="#fff" stroke-width="2.5"/><path d="M9 13l5 5 12-14" fill="none" stroke="#fff" stroke-width="3"/></svg>Hosted Servers</li>
      <li><svg viewBox="0 0 30 30"><rect x="3" y="3" width="18" height="18" fill="none" stroke="#fff" stroke-width="2.5"/><path d="M9 13l5 5 12-14" fill="none" stroke="#fff" stroke-width="3"/></svg>Virtual Desktop</li>
      <li><svg viewBox="0 0 30 30"><rect x="3" y="3" width="18" height="18" fill="none" stroke="#fff" stroke-width="2.5"/><path d="M9 13l5 5 12-14" fill="none" stroke="#fff" stroke-width="3"/></svg>VoIP/Unified Communications</li>
      <li><svg viewBox="0 0 30 30"><rect x="3" y="3" width="18" height="18" fill="none" stroke="#fff" stroke-width="2.5"/><path d="M9 13l5 5 12-14" fill="none" stroke="#fff" stroke-width="3"/></svg>Hosted Email/MailHub</li>
      <li><svg viewBox="0 0 30 30"><rect x="3" y="3" width="18" height="18" fill="none" stroke="#fff" stroke-width="2.5"/><path d="M9 13l5 5 12-14" fill="none" stroke="#fff" stroke-width="3"/></svg>Sentinel+/Email Security</li>
      <li><svg viewBox="0 0 30 30"><rect x="3" y="3" width="18" height="18" fill="none" stroke="#fff" stroke-width="2.5"/><path d="M9 13l5 5 12-14" fill="none" stroke="#fff" stroke-width="3"/></svg>Hosted Monitoring</li>
      <li><svg viewBox="0 0 30 30"><rect x="3" y="3" width="18" height="18" fill="none" stroke="#fff" stroke-width="2.5"/><path d="M9 13l5 5 12-14" fill="none" stroke="#fff" stroke-width="3"/></svg>Online Backups</li>
      <li><svg viewBox="0 0 30 30"><rect x="3" y="3" width="18" height="18" fill="none" stroke="#fff" stroke-width="2.5"/><path d="M9 13l5 5 12-14" fill="none" stroke="#fff" stroke-width="3"/></svg>DRaaS, IaaS, PaaS</li>
      <li><svg viewBox="0 0 30 30"><rect x="3" y="3" width="18" height="18" fill="none" stroke="#fff" stroke-width="2.5"/><path d="M9 13l5 5 12-14" fill="none" stroke="#fff" stroke-width="3"/></svg>Cloud Networking</li>
      <li><svg viewBox="0 0 30 30"><rect x="3" y="3" width="18" height="18" fill="none" stroke="#fff" stroke-width="2.5"/><path d="M9 13l5 5 12-14" fill="none" stroke="#fff" stroke-width="3"/></svg>Data Center Services</li>
      <li><svg viewBox="0 0 30 30"><rect x="3" y="3" width="18" height="18" fill="none" stroke="#fff" stroke-width="2.5"/><path d="M9 13l5 5 12-14" fill="none" stroke="#fff" stroke-width="3"/></svg>UniTalk / TeamVoice for Business</li>
    </ul>

    <div class="feature-icons">
      <div class="feature-icon">
        <svg viewBox="0 0 110 110" fill="none" stroke="#fff" stroke-width="5">
          <circle cx="55" cy="28" r="13"/><path d="M32 66c0-14 10-22 23-22s23 8 23 22"/>
          <circle cx="22" cy="60" r="9"/><circle cx="88" cy="60" r="9"/>
          <path d="M6 94c0-10 7-16 16-16s16 6 16 16M72 94c0-10 7-16 16-16s16 6 16 16"/>
        </svg>
      </div>
      <div class="feature-icon">
        <svg viewBox="0 0 110 110" fill="none" stroke="#fff" stroke-width="6">
          <circle cx="42" cy="58" r="22"/><circle cx="42" cy="58" r="8"/>
          <path d="M42 28v-8M42 96v-8M12 58h-8M80 58h-8M21 37l-6-6M69 85l-6-6M21 79l-6 6M69 31l-6 6"/>
          <circle cx="84" cy="26" r="12"/><circle cx="84" cy="26" r="4"/>
        </svg>
      </div>
      <div class="feature-icon">
        <svg viewBox="0 0 110 110" fill="none" stroke="#fff" stroke-width="5">
          <path d="M28 62a18 18 0 0 1 4-35 24 24 0 0 1 46 4 16 16 0 0 1 4 31"/>
          <path d="M55 44v52M38 80l17 17 17-17"/>
        </svg>
      </div>
    </div>
  </section>

  <div class="phone-band">555.010.4827</div>

  <footer class="footer">
    <span class="footer-web">www.brisalinksys.com</span>
    <span class="footer-name">BrisaLink Systems Corp</span>
  </footer>
</main>
</body>
</html>
```